依頼詳細
12月1日の開催である為、クリスマスをイメージした上品なデザインで、配色はゴールドや赤色を希望しています。ターゲットは50代~70代のハイクラスな女性です。

記載項目
添付資料の通り、ご記載下さいませ。
サイズ
A4
ページ数
片面
希望イメージ
シンプル 複雑
単色 カラフル
暗い 明るい
日常 高級
遊び心 厳粛
未来的 伝統的
女性的 男性的
希望する色
赤系、ゴールドを思わせる色調を希望。
納品ファイル
• 高解像度JPG (.jpg)
• イラストレーター形式 (.ai)
補足説明
【チラシを御考案下さる皆様へ】

いつも素敵なデザインをご提案下さいまして、誠にありがとうございます。
この度は、第6回目となります「のびのび鍵盤フェスタin岡山」のチラシデザインをお願いしたいと存じます。
出演者の皆様は、1分15秒のステージに向けて一生懸命に練習をされていますので、このチラシで出演者様もご来場者様もワクワクしていただけますと幸いに存じます。
どうぞ宜しくお願い申し上げます。

by.全国のびのび鍵盤連盟
追記:添付ファイルをご参照下さいませ。
大変素敵な御提案を下さり、誠にありがとうございます。
既に数点、感謝しつつ拝見しております。

背景についてですが、
必ずしもグランドピアノが必要であるとは思っておりません。
音楽に拘らず、クリスマスの雰囲気でワクワク上品な雰囲気であれば、
何ら問題ございません。

どうぞ宜しくお願い申し上げます。
【デザインをご考案頂きました皆様へ】

この度は、「熟年キーボード音楽祭・フライヤー」のデザインをご考案頂きまして、誠にありがとうございました。

本当に素晴らしい作品ばかりで、胸がジーンとしてまいります。

心から感謝申し上げます。

現在ご提案頂きました作品一点一点を、関係者と共に選定中でございます。

何卒宜しくお願い申し上げます。

取り急ぎ御礼まで。

全国のびのび鍵盤連盟
■ 選んだ理由

この作品は、落ち着いた赤色の中にも、華やかさがある大人のクリスマスを感じさせるデザインで、ピアノ講師陣の一番人気の作品でした。全体のイメージが何かが起こりそうな楽しい予感を感じ、文字も大変読みやすいデザインです。この様なチラシを皆様に配りすることが出来、大変嬉しく思っております。改めまして御礼申し上げます。

■ 提案者全員のお礼・コメント

この度は、「熟年キーボード音楽祭・フライヤー」のデザインをご考案下さいまして、誠にありがとうございます。デザイナー様のお一人お一人の熱い想いのこもった数々の作品に、本当に胸が一杯でございます。クリスマスのイメージはもちろんですが、60代から70代の年齢に合わせて読みやすくなさって下さったり、書体の工夫。。と細部にわたるご配慮、改めまして心より御礼申し上げます。今後もイベントに合わせてコンペ方式でデザインのご提案を依頼させて頂くことがございますので、引き続き宜しくお願い申し上げます!

```html
<!DOCTYPE html>
<html lang="ja">
<head>
<meta charset="utf-8">
<title>のびのび鍵盤フェスタin岡山</title>
<link rel="stylesheet" href="https://fonts.googleapis.com/css2?family=Noto+Serif+JP:wght@400;600;700;900&family=Shippori+Mincho+B1:wght@700;800&display=swap">
<style>
:root{
  --coral:#d9796c;
  --coral-light:#f3c2b8;
  --ink:#2b1a14;
  --gold-dark:#7d4f24;
  --gold-light:#c9995e;
  --box-fill:#f7dcd6;
  --box-edge:#e9b0a4;
  --red:#d3242a;
  --line:#333;
}
*{box-sizing:border-box;margin:0;padding:0}
html,body{width:849px;height:1200px;overflow:hidden;background:#fff}
body{font-family:"Noto Serif JP",serif;color:var(--ink);position:relative}
.flyer{position:absolute;inset:0;width:849px;height:1200px;overflow:hidden}
.hero{position:absolute;left:0;top:0;width:849px;height:850px;
  background:radial-gradient(ellipse 60% 45% at 45% 42%,var(--coral-light) 0%,#e99a8c 55%,var(--coral) 100%)}
.deco{position:absolute}
.deco-pearls{left:500px;top:0;width:349px;height:290px}
.deco-snow-left{left:0;top:560px;width:90px;height:280px;border-radius:0 60px 60px 0;
  background:radial-gradient(ellipse at 20% 50%,rgba(255,255,255,.55),rgba(255,255,255,0) 70%)}
.deco-snow-right{left:680px;top:40px;width:160px;height:170px;border-radius:50%;
  background:radial-gradient(circle,rgba(255,255,255,.5),rgba(255,255,255,0) 70%)}
.abs{position:absolute;white-space:nowrap}
.recruit{left:42px;top:24px;font-size:24px;font-weight:700;letter-spacing:1px}
.stage-sub{left:654px;top:34px;font-size:20px;font-weight:600}
.stage{left:654px;top:66px;font-size:40px;font-weight:900;letter-spacing:2px}
.title{font-family:"Shippori Mincho B1",serif;font-weight:800;font-size:76px;line-height:1;
  background:linear-gradient(180deg,var(--gold-light),var(--gold-dark));
  -webkit-background-clip:text;background-clip:text;color:transparent;letter-spacing:2px}
.title-1{left:38px;top:86px}
.title-2{left:38px;top:160px}
.lead{font-size:17px;font-weight:600}
.lead-1{left:216px;top:238px}
.lead-2{right:96px;top:264px}
.date{left:42px;top:298px;font-weight:900;font-size:40px;line-height:1}
.date .big{font-size:62px}
.venue{left:44px;top:378px;font-size:24px;font-weight:900}
.venue .time{font-size:19px;margin-left:40px;letter-spacing:3px}
.box{position:absolute;background:var(--box-fill);border:3px solid var(--box-edge);border-radius:16px;
  font-size:13.5px;line-height:1.35}
.box-grade{left:24px;top:429px;width:394px;height:216px;padding:14px 30px}
.box-free{left:440px;top:429px;width:396px;height:93px;padding:10px 22px}
.box-group{left:440px;top:531px;width:396px;height:114px;padding:6px 22px;line-height:1.28}
.box h3{font-size:16px;font-weight:700;margin-bottom:8px}
.box-group h3{margin-bottom:5px}
.box-grade h3{padding-left:10px;line-height:1.55;margin-bottom:18px}
.box-grade .label{margin-top:14px}
.notes{left:26px;top:652px;font-size:8.6px;line-height:1.3}
.org{left:24px;top:722px;display:flex;align-items:center;gap:10px}
.org-dot{width:58px;height:58px;border-radius:50%;background:#6f8f2a}
.org-name{font-size:19px;font-weight:700;line-height:1.25}
.box-pay{left:440px;top:703px;width:396px;height:95px;padding:6px 14px;font-size:8.8px;line-height:1.45}
.box-pay h4{text-align:center;font-size:11px;font-weight:700;margin-bottom:4px}
.box-pay .bank{margin-top:6px}
.sponsors{left:26px;top:800px;font-size:8.2px;line-height:1.4;white-space:normal;width:720px}
.cut{left:334px;top:853px;font-size:8.5px}
.form-head{left:10px;top:866px;font-size:19px;font-weight:900;line-height:1.3}
.form-head .deadline{color:var(--red)}
.form-note{left:358px;top:872px;font-size:11px}
.form{position:absolute;left:0;top:0;width:849px;height:1200px}
.cell{position:absolute;font-size:13px;font-weight:700;white-space:nowrap}
.small{font-size:11px;font-weight:400}
.box-mark{display:inline-block;width:11px;height:11px;border:1px solid var(--line);margin-right:3px;vertical-align:-1px}
</style>
</head>
<body>
<main class="flyer">
  <section class="hero">
    <svg class="deco deco-pearls" role="img" aria-label="斜めに流れる真珠のネックレスの装飾" viewBox="0 0 349 290">
      <defs>
        <linearGradient id="pearlBand" x1="0" y1="0" x2="1" y2="1">
          <stop offset="0" stop-color="#f4eeea" stop-opacity=".75"/>
          <stop offset="1" stop-color="#e9d8d2" stop-opacity=".55"/>
        </linearGradient>
      </defs>
      <path d="M20 0 L80 0 Q160 130 349 200 L349 270 Q140 190 20 0 Z" fill="url(#pearlBand)"/>
    </svg>
    <div class="deco deco-snow-right" role="img" aria-label="雪の結晶の装飾"></div>
    <div class="deco deco-snow-left" role="img" aria-label="雪の結晶の装飾"></div>

    <p class="abs recruit">趣味で楽しみたい演奏者　大募集！</p>
    <p class="abs stage-sub">1分15秒の</p>
    <p class="abs stage">花舞台</p>

    <h1>
      <span class="abs title title-1">のびのび鍵盤</span>
      <span class="abs title title-2">フェスタ in 岡山</span>
    </h1>
    <p class="abs lead lead-1">「ここまで弾けた！」その喜びを１分１５秒に込めて・・・</p>
    <p class="abs lead lead-2">貴方のお好きな曲でチャレンジしてみませんか</p>

    <p class="abs date">2015年<span class="big">12</span>月<span class="big">1</span>日(火)</p>
    <p class="abs venue">晴海新報本社ひかりホール<span class="time">開場　11：30　開演　12：00</span></p>

    <div class="box box-grade">
      <h3>「のびのび鍵盤<br>　　グレード認定４７」部門</h3>
      <p>【演奏時間】 1分１５秒以内</p>
      <p class="label">【参加費】</p>
      <p>①課題１つを選択　5,940円（税込）</p>
      <p>②課題２つを選択　6,480円（税込）</p>
      <p>③課題３つを選択　7,020円（税込）</p>
    </div>
    <div class="box box-free">
      <h3>自由演奏部門</h3>
      <p>【演奏時間】 1分１５秒以内</p>
      <p>【参加費】　 5,040円（税込）</p>
    </div>
    <div class="box box-group">
      <h3>グループ演奏部門</h3>
      <p>【演奏時間】</p>
      <p>2名で演奏　2分１５秒以内</p>
      <p>3名以上で演奏 2分３０秒以内</p>
      <p>【１名あたり参加費】3,780円（税込）</p>
    </div>

    <div class="abs notes">
      ■お申し込み方法/各担当講師に直接ご連絡ください。<br>
      ※追って詳細（入金方法・出演について）のご案内をお伝え致します。<br>
      ■お問い合せ先/〒530-0099 大阪府大阪市北区架空町1番2号 みどりビル8階<br>
      一般社団法人 全国のびのび鍵盤連盟「のびのび鍵盤フェスタin岡山」実行委員会　宛<br>
      TEL：06-0000-1234　FAX：06-0000-1235　Email：info@nobinobi-kenban.example(担当:森田)
    </div>

    <div class="abs org">
      <span class="org-dot"></span>
      <span class="org-name">一般社団法人<br>全国のびのび鍵盤連盟</span>
    </div>

    <div class="box box-pay">
      <h4>〜参加費につきまして〜</h4>
      <p>●参加費は申込み時にお振込みください。尚、返金はいかなる場合も不可となります。</p>
      <p class="bank">みらい銀行　岡山支店</p>
      <p>普通 ０１２３４５　全国のびのび鍵盤連盟</p>
      <p>※振込手数料は各自ご負担にてお願い致します。</p>
    </div>

    <p class="abs sponsors">■主催/一般社団法人 全国のびのび鍵盤連盟<br>
      ■後援/あさひ市教育委員会・みどり市教育委員会・つばさ町教育委員会・はるか市教育委員会・こだま市教育委員会・さくら市教育委員会・さくら文化連盟・なぎさ市教育委員会・かえで市教育委員会・しらゆき市教育委員会・ひので市教育委員会・このは町教育委員会・ゆうなぎ市教育委員会・晴海新報社・瀬戸テレビ・みなと放送・(株)あおば楽器店・ソナタミュージック(株)</p>
  </section>

  <p class="abs cut">（こちらから切り取ってお申込みください。）</p>
  <p class="abs form-head">参加申込書/<span class="deadline">１０月２日（金）締切</span></p>
  <p class="abs form-note">※「のびのび鍵盤」教室の方は、担当講師に申込書と参加費を直接お渡しください。</p>

  <svg class="form" viewBox="0 0 849 1200" aria-hidden="true">
    <g stroke="var(--line)" stroke-width="1.2" fill="none">
      <line x1="0" y1="897" x2="849" y2="897"/>
      <line x1="0" y1="968" x2="363" y2="968"/>
      <line x1="0" y1="993" x2="849" y2="993"/>
      <line x1="363" y1="897" x2="363" y2="993"/>
      <line x1="701" y1="897" x2="701" y2="993"/>
      <line x1="0" y1="1015" x2="849" y2="1015"/>
      <line x1="0" y1="1053" x2="849" y2="1053"/>
      <line x1="368" y1="1015" x2="368" y2="1053"/>
      <line x1="627" y1="1015" x2="627" y2="1200"/>
      <line x1="70" y1="1053" x2="70" y2="1200"/>
      <line x1="392" y1="1053" x2="392" y2="1200"/>
      <line x1="229" y1="1090" x2="229" y2="1200"/>
      <line x1="627" y1="1125" x2="849" y2="1125"/>
      <line x1="85" y1="1126" x2="220" y2="1126"/>
      <line x1="240" y1="1126" x2="385" y2="1126"/>
      <line x1="85" y1="1160" x2="220" y2="1160"/>
      <line x1="240" y1="1160" x2="385" y2="1160"/>
      <line x1="85" y1="1192" x2="220" y2="1192"/>
      <line x1="240" y1="1192" x2="385" y2="1192"/>
    </g>
  </svg>

  <span class="cell small" style="left:18px;top:900px">ふりがな</span>
  <span class="cell" style="left:16px;top:931px">お名前</span>
  <span class="cell" style="left:14px;top:973px">電話番号<span style="margin-left:90px">—</span><span style="margin-left:70px">—</span></span>
  <span class="cell" style="left:370px;top:903px">ご住所　　(〒　　—　　　)</span>
  <span class="cell" style="left:735px;top:903px">課題クリア数</span>
  <span class="cell" style="left:18px;top:1026px">曲目</span>
  <span class="cell" style="left:376px;top:1026px">作曲者名</span>
  <span class="cell" style="left:640px;top:1026px">演奏時間<span style="margin-left:64px">分</span><span style="margin-left:46px">秒</span></span>
  <span class="cell" style="left:8px;top:1062px">参加部門</span>
  <span class="cell small" style="left:4px;top:1100px;font-size:9.5px;line-height:1.55">参加部門に<br>✓印をつけて<br>ください</span>
  <span class="cell" style="left:108px;top:1062px"><span class="box-mark"></span>のびのび鍵盤グレード認定47部門</span>
  <span class="cell small" style="left:78px;top:1110px">①県名：</span>
  <span class="cell small" style="left:242px;top:1110px">課題：</span>
  <span class="cell small" style="left:78px;top:1144px">②県名：</span>
  <span class="cell small" style="left:242px;top:1144px">課題：</span>
  <span class="cell small" style="left:78px;top:1176px">③県名：</span>
  <span class="cell small" style="left:242px;top:1176px">課題：</span>
  <span class="cell" style="left:424px;top:1078px"><span class="box-mark"></span>自由演奏部門</span>
  <span class="cell" style="left:424px;top:1157px"><span class="box-mark"></span>グループ演奏部門</span>
  <span class="cell" style="left:710px;top:1060px">担当講師</span>
  <span class="cell" style="left:685px;top:1133px">ピアノ鍵盤シール</span>
  <span class="cell" style="left:676px;top:1160px">必要　　・　　不要</span>
</main>
</body>
</html>
```